Print Ad for Pilates Studio

I need a full color 1/4 page ad (size 5" tall x 3 3/4" wide) that includes our logo at top with this text:
Intro Specials for New Students:
3 Private Sessions for only $150 (normally $75/session)
3 Group Reformer Classes for $49 (normally $35/class)
5 Bootcamp Classes for only $29 (normally $15/class0
and might include the tree graphic, and the three small logos (QRT, Green-certified and Best of) at bottom plus our phone number really big
555-247-9136 and e-mail MarthaWendlock@mailverra.com and website www.swaycraftstudio.biz
Should look enticing and CLEAN

Target Market(s)

Older affluent market

Industry/Entity Type

Group

Requirements
Must have
• Clean lines
• Bold
• Classy
• some space
• Makes you want to take action now
Nice to have
• photo of people doing pilates
• Bold color like yellow, green, burgundy

```html
<!DOCTYPE html>
<html lang="en">
<head>
<meta charset="utf-8">
<title>Swaycraft – Intro Specials</title>
<link rel="stylesheet" href="https://fonts.googleapis.com/css2?family=Dosis:wght@500;600&family=Roboto+Condensed:wght@400;700&family=Lato:wght@700&display=swap">
<style>
  :root {
    --paper: #f4f4f2;
    --leaf: #3f7a2c;
    --forest-deep: #1f3f18;
    --gold: #c99a3a;
    --gold-light: #e0b95a;
    --white: #ffffff;
    --photo-a: #ececea;
    --photo-b: #bdbdba;
  }
  html, body { margin: 0; padding: 0; overflow: hidden; background: var(--white); }
  .ad {
    position: relative;
    width: 901px;
    height: 1200px;
    overflow: hidden;
    font-family: "Roboto Condensed", sans-serif;
    color: var(--white);
  }
  .ad__backdrop { position: absolute; inset: 0; }
  .brand__name {
    position: absolute;
    left: 112px;
    top: 30px;
    margin: 0;
    font-family: "Dosis", sans-serif;
    font-weight: 600;
    font-size: 82px;
    line-height: 1;
    color: var(--leaf);
  }
  .brand__tagline {
    position: absolute;
    left: 241px;
    top: 125px;
    width: 395px;
    height: 31px;
    background: var(--leaf);
    border-radius: 3px;
    font-family: "Lato", sans-serif;
    font-weight: 700;
    font-size: 21px;
    line-height: 31px;
    text-align: center;
    color: var(--white);
  }
  .intro {
    position: absolute;
    left: 40px;
    top: 290px;
    margin: 0;
    font-family: "Dosis", sans-serif;
    font-weight: 500;
    font-size: 56px;
    line-height: 72px;
    letter-spacing: 3px;
  }
  .offer {
    position: absolute;
    left: 32px;
    margin: 0;
    font-size: 37px;
    white-space: nowrap;
  }
  .offer__title { font-weight: 700; letter-spacing: 1px; }
  .offer__lead { font-size: 29px; }
  .offer__price { font-weight: 700; font-size: 52px; color: var(--gold-light); }
  .offer__note {
    position: absolute;
    left: 198px;
    margin: 0;
    font-size: 32px;
    letter-spacing: 0.5px;
    white-space: nowrap;
  }
  .call {
    position: absolute;
    left: 40px;
    top: 958px;
    margin: 0;
    font-size: 40px;
    white-space: nowrap;
  }
  .call__number { font-weight: 700; font-size: 72px; margin-left: 10px; letter-spacing: 1px; }
  .contact {
    position: absolute;
    left: 62px;
    top: 1080px;
    margin: 0;
    font-weight: 700;
    font-size: 28px;
    line-height: 46px;
    letter-spacing: 0.5px;
  }
</style>
</head>
<body>
<main class="ad">
  <svg class="ad__backdrop" width="901" height="1200" viewBox="0 0 901 1200">
    <defs>
      <linearGradient id="fieldGrad" x1="0" y1="0" x2="0" y2="1">
        <stop offset="0" stop-color="#2f5e22"/>
        <stop offset="0.5" stop-color="#5e9a3d"/>
        <stop offset="1" stop-color="#4f8633"/>
      </linearGradient>
      <linearGradient id="bandGrad" x1="0" y1="0" x2="0" y2="1">
        <stop offset="0" stop-color="#2c5a22"/>
        <stop offset="1" stop-color="#1f4318"/>
      </linearGradient>
      <radialGradient id="photoGrad" cx="0.6" cy="0.4" r="0.7">
        <stop offset="0" stop-color="var(--photo-a)"/>
        <stop offset="1" stop-color="var(--photo-b)"/>
      </radialGradient>
      <radialGradient id="treeGrad" cx="0.5" cy="0.5" r="0.5">
        <stop offset="0" stop-color="#3a6d28" stop-opacity="0.7"/>
        <stop offset="0.6" stop-color="#3f7a2c" stop-opacity="0.4"/>
        <stop offset="1" stop-color="#4f8633" stop-opacity="0"/>
      </radialGradient>
    </defs>

    <rect class="paper" x="0" y="0" width="901" height="198" fill="var(--paper)"/>
    <rect class="field" x="0" y="198" width="901" height="1002" fill="url(#fieldGrad)"/>
    <rect class="rule-top" x="0" y="194" width="901" height="6" fill="var(--gold)"/>

    <ellipse class="tree" role="img" aria-label="Illustrated leafy tree growing at the right edge" cx="800" cy="720" rx="150" ry="210" fill="url(#treeGrad)"/>

    <circle cx="720" cy="340" r="272" fill="var(--gold)"/>
    <circle class="photo" role="img" aria-label="Photo of two women exercising on Pilates reformers with legs raised in straps" cx="720" cy="340" r="266" fill="url(#photoGrad)"/>

    <g class="offer-bands">
      <polygon points="0,535 604,535 576,655 0,655" fill="url(#bandGrad)"/>
      <polygon points="604,535 576,655 562,655 590,560" fill="var(--gold)"/>
      <polygon points="0,672 604,672 576,795 0,795" fill="url(#bandGrad)"/>
      <polygon points="604,672 576,795 562,795 590,697" fill="var(--gold)"/>
      <polygon points="0,812 604,812 576,935 0,935" fill="url(#bandGrad)"/>
      <polygon points="604,812 576,935 562,935 590,837" fill="var(--gold)"/>
    </g>

    <path class="sweep" d="M0,1050 C300,1062 640,1040 901,935 L901,1200 L0,1200 Z" fill="var(--gold)"/>
    <path class="footer" d="M0,1062 C300,1074 640,1054 901,950 L901,1200 L0,1200 Z" fill="var(--forest-deep)"/>

    <g class="badges">
      <rect x="550" y="1063" width="106" height="102" rx="4" fill="var(--white)"/>
      <rect x="667" y="1063" width="102" height="102" rx="6" fill="#dfe6ee"/>
      <rect x="778" y="1063" width="92" height="102" rx="6" fill="#2b5fae"/>
    </g>
  </svg>

  <p class="brand__name">swaycraft</p>
  <div class="brand__tagline">Pilates &amp; Spiral Motion Studio</div>

  <h1 class="intro">Intro<br>Specials for<br>New Students:</h1>

  <p class="offer" style="top:548px"><span class="offer__title">3 Private Sessions</span> <span class="offer__lead">for only</span> <span class="offer__price">$150</span></p>
  <p class="offer__note" style="top:606px">(Normally $ 75/Session)</p>

  <p class="offer" style="top:686px"><span class="offer__title">3 Group Reformer</span> <span class="offer__lead">for only</span> <span class="offer__price">$49</span></p>
  <p class="offer__note" style="top:744px">(Normally $ 35/Session)</p>

  <p class="offer" style="top:825px"><span class="offer__title">5 Bootcamp Classes</span> <span class="offer__lead">for only</span> <span class="offer__price">$29</span></p>
  <p class="offer__note" style="top:882px">(Normally $ 15/Class)</p>

  <p class="call">Call US :<span class="call__number">555-247-9136</span></p>

  <p class="contact">MarthaWendlock@mailverra.com<br>www.swaycraftstudio.biz</p>
</main>
</body>
</html>
```